K P Guard Services - Alarm and CCTV installation Flyer

Need a flyer designed that grabs the attention of potential customers, we need the price to stand out the most to grab people’s attention, whether they are residential or commercial.We are a security company based in Brentwood Essex but cover London and the home counties. here is our website to take a look at www.kpguardservices.co.uk. We want them to know we install complete alarm and Cctv systems and will keep them “safe”

Target Market(s)

residential and commercial property

Colors
f37122

Requirements
Must have
• on one side
• large clear logo - professional design
• - Intruder Alarms starting from £495 + VAT. (Big text)
• - £150 discount on installations
• *terms and conditions apply (small text)
• - Not happy with your current provider? Free of charge no obligation take over survey and quotation and up to £100 off
• - CCTV systems starting from £595 + VAT (based on 2 cameras)
• K P Guard Services are always there, always available, wherever and whenever you need us.
• Large telephone number at the bottom 01632 480913
• Address / email / website as a footer * see website for details
• on second side
• large and bold
• Are you looking to keep you and your premises safe?
• - K P Guard Services install, maintain and repair all intruder alarms, CCTV, intercom and access control
• - View, control and manage your security systems anywhere in the world
• - Feel at ease with monitoring services & police response tailored to suit you and your business
• - K P Guard can takeover any existing security system and offer maintenance checks to guarantee the best performance for you and your premises
• - K P Guard understand that being security conscious is ever increasing, protecting your property and family is a number one priority
• - Our fully insured and accredited team offer quality, safety and cost efficiency throughout the whole process
• - K P Guard Services are using the latest cloud-based technology to stay connected with your home and business 24/7
• If you are looking to improve the security in your home, office or commercial property then call a member of our team today for a free quote.
• Fully insured and accredited
• Jobrater logo and NQRB Intruder and CCTV logos
• Logo somewhere on page and
• Telephone number
• Address / email / website as footer
Nice to have
• We would like to have the text saying
• Intruder alarms installed from £495 + vat the biggest text on the page. Most likely the £495 part the largest.
• Also would like “not happy with your current provider” more obvious
• We would like use our company colours - Orange/White/black

```html
<!DOCTYPE html>
<html lang="en">
<head>
<meta charset="UTF-8">
<title>K P Guard Services – Alarm and CCTV Flyer</title>
<link rel="stylesheet" href="https://fonts.googleapis.com/css2?family=Montserrat:wght@500;600;700;800&family=Open+Sans:wght@400;600;700&display=swap">
<style>
  :root{
    --orange:#f37122;
    --charcoal:#3d3d3f;
    --ink:#2b2b2b;
    --backdrop:#38383a;
    --white:#ffffff;
  }
  *{box-sizing:border-box;margin:0;padding:0}
  html,body{width:1200px;height:866px;overflow:hidden}
  body{background:var(--backdrop);font-family:"Open Sans",Arial,sans-serif;color:var(--ink);position:relative}
  .flyer{position:absolute;top:37px;width:560px;height:792px;background:var(--white);overflow:hidden;box-shadow:0 6px 24px rgba(0,0,0,.45)}
  .flyer--front{left:30px}
  .flyer--back{left:610px}
  .layer{position:absolute;left:0;top:0}
  .logo{position:absolute;display:flex;align-items:center;gap:8px;font-family:"Montserrat",sans-serif;font-weight:700;color:var(--orange);font-size:19px;line-height:1.05;text-align:center}
  .logo__mark{width:26px;height:26px;background:var(--orange);flex:none}
  .front-logo{right:22px;top:26px}
  .back-logo{right:26px;top:22px;font-size:17px}

  .headline{position:absolute;left:30px;top:282px;font-family:"Montserrat",sans-serif;font-weight:800;color:var(--orange);font-size:39px;letter-spacing:.5px}
  .region{position:absolute;left:30px;top:330px;font-family:"Montserrat",sans-serif;font-weight:700;font-size:25px;color:var(--ink);letter-spacing:.5px}
  .price{position:absolute;left:30px;top:366px;font-family:"Montserrat",sans-serif;font-weight:700;font-size:21px;color:var(--orange)}
  .offers{position:absolute;left:30px;top:405px;width:500px;list-style:none;font-size:14px;font-weight:600;line-height:1.3}
  .offers li{display:flex;gap:10px;margin-bottom:9px}
  .offers svg{flex:none;margin-top:3px}
  .discount{color:var(--orange);font-family:"Montserrat",sans-serif;font-weight:800;font-size:20px}
  .terms{display:block;font-size:8px;font-weight:400;margin-top:1px}
  .band{position:absolute;background:var(--orange);color:var(--white);font-family:"Montserrat",sans-serif;font-weight:700}
  .front-band{left:0;top:552px;width:560px;height:62px;padding:9px 30px;font-size:17px;line-height:1.3}
  .thumbs{position:absolute;left:30px;top:628px;display:flex;gap:12px}
  .thumbs svg{border:3px solid var(--orange)}
  .footer{position:absolute;left:0;background:var(--charcoal);color:var(--white);display:flex;align-items:center}
  .front-footer{top:730px;height:62px;width:560px;padding:0 18px}
  .phone{display:flex;align-items:center;gap:10px;font-family:"Montserrat",sans-serif;font-weight:700;font-size:26px;white-space:nowrap}
  .divider{width:1px;align-self:stretch;background:#8a8a8a;margin:10px 14px}
  .contact{font-size:10.5px;line-height:1.9;white-space:nowrap}
  .contact div{display:flex;align-items:center;gap:7px}

  .question{position:absolute;left:0;top:0;width:360px;height:56px;padding:12px 0 0 26px;font-family:"Montserrat",sans-serif;font-weight:800;font-size:13px;line-height:1.2;color:var(--white)}
  .services{position:absolute;left:30px;top:252px;width:505px;list-style:none;font-size:12px;line-height:1.3}
  .services li{display:flex;gap:12px;margin-bottom:5px}
  .services .dot{flex:none;width:9px;height:9px;border-radius:50%;background:var(--orange);margin-top:4px}
  .back-band{left:18px;top:494px;width:542px;height:78px;padding:10px 26px;font-size:14px;line-height:1.35;text-transform:uppercase}
  .accreditation{position:absolute;left:38px;top:582px;display:flex;align-items:flex-start;gap:16px}
  .badge{display:flex;flex-direction:column;align-items:center;gap:3px;font-size:6.5px;text-align:center;white-space:nowrap;width:48px}
  .badge__seal{width:30px;height:30px;border-radius:50%;border:3px double #4a5a78;background:#eef1f6}
  .badge__plain{width:86px;height:26px;border-radius:4px;background:#fbe3d3;margin-top:2px}
  .insured-tab{left:270px;top:586px}
  .insured{position:absolute;left:270px;top:586px;width:290px;height:40px;padding:12px 0 0 34px;font-family:"Montserrat",sans-serif;font-weight:700;font-size:13px;color:var(--white);white-space:nowrap}
  .back-footer{top:626px;height:122px;width:560px;padding:0 24px;align-items:center}
  .back-footer .left{display:flex;flex-direction:column;gap:12px}
  .back-footer .right{font-size:12px;line-height:1.5}
  .back-footer .email{display:flex;align-items:center;gap:10px;font-size:12px}
  .follow{display:flex;align-items:center;gap:6px;font-weight:700;margin-top:8px}
  .follow span.c{width:12px;height:12px;border-radius:50%;background:#cfcfcf}
</style>
</head>
<body>

<section class="flyer flyer--front">
  <svg class="layer" width="560" height="300" viewBox="0 0 560 300">
    <defs>
      <linearGradient id="keypadTone" x1="0" y1="0" x2="1" y2="1">
        <stop offset="0" stop-color="#dfe3e7"/><stop offset="1" stop-color="#6d7780"/>
      </linearGradient>
      <linearGradient id="appTone" x1="0" y1="0" x2="1" y2="1">
        <stop offset="0" stop-color="#cfe6f6"/><stop offset="1" stop-color="#2f6fa3"/>
      </linearGradient>
    </defs>
    <polygon points="0,0 560,0 560,120 320,262 0,190" fill="url(#keypadTone)" role="img" aria-label="Photo of an alarm control keypad with a welcome screen"/>
    <polygon points="360,0 560,0 560,110 390,110" fill="var(--white)"/>
    <line x1="390" y1="110" x2="560" y2="110" stroke="var(--orange)" stroke-width="3"/>
    <line x1="0" y1="190" x2="320" y2="262" stroke="var(--orange)" stroke-width="7"/>
    <line x1="320" y1="262" x2="560" y2="120" stroke="var(--charcoal)" stroke-width="7"/>
    <circle cx="440" cy="200" r="76" fill="var(--white)"/>
    <circle cx="440" cy="200" r="70" fill="url(#appTone)" stroke="var(--orange)" stroke-width="5" role="img" aria-label="Photo of two smartphones showing the security control app"/>
  </svg>
  <div class="logo front-logo"><span class="logo__mark"></span><span>K P GUARD<br>SERVICES</span></div>

  <h1 class="headline">KP GUARD SERVICES</h1>
  <p class="region">LONDON AND HOME COUNTIES</p>
  <p class="price">Intruder Alarms starting from £495 + VAT.</p>

  <ul class="offers">
    <li><svg width="13" height="13" viewBox="0 0 13 13"><circle cx="6.5" cy="6.5" r="6.5" fill="var(--ink)"/><polyline points="3.5,6.8 5.7,9 9.6,4.3" fill="none" stroke="#fff" stroke-width="1.6"/></svg>
      <span>Not happy with your current provider? Free of charge no obligation take over survey and quotation and up to £100 off</span></li>
    <li><svg width="13" height="13" viewBox="0 0 13 13"><circle cx="6.5" cy="6.5" r="6.5" fill="var(--ink)"/><polyline points="3.5,6.8 5.7,9 9.6,4.3" fill="none" stroke="#fff" stroke-width="1.6"/></svg>
      <span><span class="discount">£150 discount</span> on installations<span class="terms">*terms and conditions apply</span></span></li>
    <li><svg width="13" height="13" viewBox="0 0 13 13"><circle cx="6.5" cy="6.5" r="6.5" fill="var(--ink)"/><polyline points="3.5,6.8 5.7,9 9.6,4.3" fill="none" stroke="#fff" stroke-width="1.6"/></svg>
      <span>CCTV systems starting from £595 + VAT (based on 2 cameras)</span></li>
  </ul>

  <p class="band front-band">K P Guard Services are always there, always available, wherever and whenever you need us.</p>

  <div class="thumbs">
    <svg width="157" height="86" role="img" aria-label="Photo of an alarm keypad in a hallway"><rect width="157" height="86" fill="#8c949b"/></svg>
    <svg width="157" height="86" role="img" aria-label="Photo of a hand entering a code on a wall alarm panel"><rect width="157" height="86" fill="#c9c3bb"/></svg>
    <svg width="157" height="86" role="img" aria-label="Photo of a touchscreen security panel in a kitchen"><rect width="157" height="86" fill="#b8bfc4"/></svg>
  </div>

  <footer class="footer front-footer">
    <div class="phone">
      <svg width="24" height="24" viewBox="0 0 24 24"><circle cx="12" cy="12" r="11" fill="none" stroke="#fff" stroke-width="2"/><path d="M8 6.5l2 2.5-1.2 1.4c.8 1.7 2 2.9 3.8 3.8l1.4-1.2 2.5 2-1.3 2.2c-4.2-.4-8.3-4.5-8.7-8.7z" fill="#fff"/></svg>
      01632 480913
    </div>
    <span class="divider"></span>
    <div class="contact">
      <div><svg width="16" height="14" viewBox="0 0 18 15"><polygon points="9,0 18,8 15,8 15,15 3,15 3,8 0,8" fill="var(--orange)"/></svg>14 Elmfield Road, Brentwood, Essex, CM14 9ZZ</div>
      <div><svg width="16" height="12" viewBox="0 0 18 13"><rect width="18" height="13" fill="var(--orange)"/><polyline points="0,0 9,7 18,0" fill="none" stroke="#fff" stroke-width="1.4"/></svg>operations@kpguardservices.co.uk</div>
    </div>
  </footer>
</section>

<section class="flyer flyer--back">
  <svg class="layer" width="560" height="260" viewBox="0 0 560 260">
    <defs>
      <linearGradient id="cameraTone" x1="0" y1="0" x2="1" y2="1">
        <stop offset="0" stop-color="#7d868e"/><stop offset=".5" stop-color="#c4ccd2"/><stop offset="1" stop-color="#9aa9b2"/>
      </linearGradient>
    </defs>
    <polygon points="0,56 370,56 390,95 560,95 560,140 290,240 0,175" fill="url(#cameraTone)" role="img" aria-label="Photo of a wall-mounted CCTV camera"/>
    <polygon points="0,0 340,0 372,56 0,56" fill="var(--orange)"/>
    <line x1="340" y1="0" x2="372" y2="56" stroke="var(--charcoal)" stroke-width="6"/>
    <line x1="290" y1="240" x2="560" y2="140" stroke="var(--orange)" stroke-width="7"/>
    <line x1="0" y1="175" x2="290" y2="240" stroke="var(--charcoal)" stroke-width="4"/>
  </svg>
  <h2 class="question">ARE YOU LOOKING TO KEEP<br>YOU AND YOUR PREMISES SAFE?</h2>
  <div class="logo back-logo"><span class="logo__mark"></span><span>K P GUARD<br>SERVICES</span></div>

  <ul class="services">
    <li><span class="dot"></span>K P Guard Services install, maintain and repair all intruder alarms, CCTV, intercom and access control</li>
    <li><span class="dot"></span>View, control and manage your security systems anywhere in the world</li>
    <li><span class="dot"></span>Feel at ease with monitoring services &amp; police response tailored to suit you and your business</li>
    <li><span class="dot"></span>K P Guard can takeover any existing security system and offer maintenance checks to guarantee the best performance for you and your premises</li>
    <li><span class="dot"></span>K P Guard understand that being security conscious is ever increasing, protecting your property and family is a number one priority</li>
    <li><span class="dot"></span>Our fully insured and accredited team offer quality, safety and cost efficiency throughout the whole process</li>
    <li><span class="dot"></span>K P Guard Services are using the latest cloud-based technology to stay connected with your home and business 24/7</li>
  </ul>

  <p class="band back-band">If you are looking to improve the security in your home, office or commercial property then call a member of our team today for a free quote.</p>

  <div class="accreditation">
    <div class="badge"><span class="badge__seal"></span>CCTV Systems</div>
    <div class="badge"><span class="badge__seal"></span>Intruder Alarm Systems</div>
    <div class="badge"><span class="badge__seal"></span></div>
    <div class="badge" style="width:86px"><span class="badge__plain"></span></div>
  </div>

  <svg class="layer insured-tab" width="290" height="40" viewBox="0 0 290 40"><polygon points="20,0 290,0 290,40 0,40" fill="var(--orange)"/></svg>
  <p class="insured">FULLY INSURED AND ACCREDITED</p>

  <footer class="footer back-footer">
    <div class="left">
      <div class="phone">
        <svg width="24" height="24" viewBox="0 0 24 24"><circle cx="12" cy="12" r="11" fill="none" stroke="#fff" stroke-width="2"/><path d="M8 6.5l2 2.5-1.2 1.4c.8 1.7 2 2.9 3.8 3.8l1.4-1.2 2.5 2-1.3 2.2c-4.2-.4-8.3-4.5-8.7-8.7z" fill="#fff"/></svg>
        01632 480913
      </div>
      <div class="email"><svg width="22" height="15" viewBox="0 0 22 15"><rect width="22" height="15" fill="var(--orange)"/><polyline points="0,0 11,8 22,0" fill="none" stroke="#fff" stroke-width="1.4"/></svg>operations@kpguardservices.co.uk</div>
    </div>
    <span class="divider"></span>
    <div class="right">
      <div style="display:flex;gap:8px"><svg width="20" height="17" viewBox="0 0 18 15"><polygon points="9,0 18,8 15,8 15,15 3,15 3,8 0,8" fill="var(--orange)"/></svg><span>14 Elmfield Road, Brentwood,<br>Essex, CM14 9ZZ</span></div>
      <div class="follow">Follow Us: <span class="c"></span><span class="c"></span><span class="c"></span></div>
    </div>
  </footer>
</section>

</body>
</html>
```